High-end dermatology office brochure design

Corvellan Skin and Laser is a high-end dermatology practice that specializes in custom skin care solutions, and skin cancer surveillance and treatment. Brochure should be elegant, but informative to attract high-end customers.

Target Market(s)

Men and women 27-60

Industry/Entity Type

Office

Requirements
Must have
• Attached document has required copy, including, websites, address and company phone number
Nice to have
• images

```html
<!DOCTYPE html>
<html lang="en">
<head>
<meta charset="utf-8">
<title>Corvellan Skin and Laser – Trifold Brochure</title>
<link href="https://fonts.googleapis.com/css2?family=Raleway:ital,wght@0,400;0,600;0,700;1,700&family=Handlee&display=swap" rel="stylesheet">
<style>
  :root{
    --purple:#6a3d8f;
    --purple-dark:#58307a;
    --lilac:#d9cde7;
    --green:#9bc53d;
    --white:#ffffff;
    --ink:#3b3b3b;
    --backdrop:#ece9ef;
    --skin-a:#f3ddd0;
    --skin-b:#d9b2a0;
  }
  *{box-sizing:border-box;margin:0;padding:0}
  html,body{width:1200px;height:900px;overflow:hidden;background:var(--backdrop);font-family:'Raleway',sans-serif;color:var(--ink)}
  .sheet{position:absolute;left:40px;width:1120px;height:420px;background:var(--white);box-shadow:0 4px 14px rgba(0,0,0,.15);overflow:hidden}
  .sheet--outside{top:20px}
  .sheet--inside{top:460px}
  .sheet svg.shapes{position:absolute;inset:0}
  .photo{position:absolute;background:linear-gradient(135deg,var(--skin-a),var(--skin-b) 70%,#b98f7f)}
  .fold{position:absolute;top:0;bottom:0;width:1px;background:rgba(0,0,0,.08)}
  .abs{position:absolute}
  .script{font-family:'Handlee',cursive;font-weight:400}
  .on-purple{color:var(--white)}
  .heading{font-size:25px;line-height:1.05}
  .body{font-size:11px;line-height:1.35}
  .center{text-align:center}
  .ticks{list-style:none;font-size:11px;line-height:1.35;font-weight:600}
  .ticks--tight{font-size:10.5px;line-height:1.22}
  .ticks li::before{content:"";display:inline-block;width:9px;height:6px;border-left:2px solid var(--green);border-bottom:2px solid var(--green);transform:rotate(-45deg) translateY(-2px);margin-right:5px}
  .location{position:absolute;width:80px;height:80px;display:flex;align-items:center;justify-content:center;text-align:center;font-size:7.5px;font-weight:700;line-height:1.18;color:var(--ink)}
  .contact{font-size:13px;font-weight:600;display:flex;align-items:center;gap:7px}
  .brand-name{font-size:15px;font-weight:700;color:var(--purple);text-align:center;line-height:1.15}
</style>
</head>
<body>

<!-- Outside of the trifold -->
<section class="sheet sheet--outside">
  <div class="photo" style="left:0;top:0;width:373px;height:200px" role="img" aria-label="Portrait photo of a woman with a hand at her cheek"></div>
  <div class="photo" style="left:746px;top:0;width:374px;height:230px" role="img" aria-label="Portrait photo of a woman with hair pulled back"></div>

  <svg class="shapes" width="1120" height="420" viewBox="0 0 1120 420">
    <path d="M0 170 Q180 140 373 190" fill="none" stroke="var(--lilac)" stroke-width="8"/>
    <path d="M0 178 Q180 150 373 198 L373 420 L0 420Z" fill="var(--purple)"/>
    <path d="M373 245 Q560 205 746 232" fill="none" stroke="var(--lilac)" stroke-width="8"/>
    <path d="M373 252 Q560 212 746 240 L746 420 L373 420Z" fill="var(--purple)"/>
    <path d="M373 372 L746 352 L746 404 L373 420Z" fill="var(--green)"/>
    <path d="M746 218 Q930 190 1120 214" fill="none" stroke="var(--lilac)" stroke-width="8"/>
    <path d="M746 226 Q930 198 1120 222 L1120 420 L746 420Z" fill="var(--purple)"/>
    <circle cx="560" cy="95" r="46" fill="var(--white)" stroke="var(--green)" stroke-width="8"/>
    <circle cx="598" cy="180" r="46" fill="var(--white)" stroke="var(--green)" stroke-width="8"/>
    <circle cx="585" cy="268" r="48" fill="var(--white)" stroke="var(--green)" stroke-width="8"/>
    <circle cx="933" cy="342" r="54" fill="var(--white)" stroke="var(--green)" stroke-width="8"/>
  </svg>
  <div class="fold" style="left:373px"></div>
  <div class="fold" style="left:746px"></div>

  <!-- Panel: nutrition -->
  <h2 class="abs script heading on-purple center" style="left:20px;top:205px;width:333px">- Nutrition and<br>supplement support -</h2>
  <p class="abs body on-purple" style="left:24px;top:268px;width:325px">Including gluten free, no filler multi-vitamins, immune boosters, hormone, sleep aid balancing products and B12 injections and the Slim Boost.</p>
  <p class="abs body on-purple center" style="left:24px;top:330px;width:325px;font-weight:700;font-style:italic">Let us create a custom skin care regimen that best fits your medical and personal needs. We pride ourselves on providing premium skin care, to patients of all ages, with an honest and attentive approach.</p>

  <!-- Panel: locations -->
  <h2 class="abs script" style="left:395px;top:14px;font-size:20px;color:var(--purple);line-height:1">- Visit Our<br>&nbsp;&nbsp;Locations -</h2>
  <div class="location" style="left:520px;top:55px"><span>Corvellan Skin<br>&amp; Laser<br>2210 E Mesa Rd<br>Building #4<br>Suite #120<br>Phoenix, AZ 85000</span></div>
  <div class="location" style="left:558px;top:140px"><span>Verdant Skin<br>Studio<br>7600 E Canyon Way<br>Suite #208<br>Scottsdale, AZ 85200</span></div>
  <div class="location" style="left:545px;top:228px"><span>Islewind Skin<br>Clinic<br>Two Harbor Plaza<br>Suite #310<br>400 Lagoon Blvd<br>Honolulu, HI 96800</span></div>
  <div class="abs on-purple" style="left:420px;top:318px">
    <div class="contact">
      <svg width="13" height="13" viewBox="0 0 24 24"><circle cx="12" cy="12" r="12" fill="var(--white)"/><path d="M8 6l2 0 1 3-1.5 1a8 8 0 0 0 4.5 4.5l1-1.5 3 1 0 2c-6 1-11-4-10-10z" fill="var(--purple)"/></svg>
      480-555-0142
    </div>
    <div class="contact" style="margin-top:6px">
      <svg width="13" height="13" viewBox="0 0 24 24"><circle cx="12" cy="12" r="10" fill="none" stroke="var(--white)" stroke-width="2"/><path d="M2 12h20M12 2c-4 5-4 15 0 20M12 2c4 5 4 15 0 20" fill="none" stroke="var(--white)" stroke-width="1.6"/></svg>
      www.corvellanskincare.com
    </div>
  </div>
  <p class="abs center" style="left:400px;top:372px;width:320px;font-size:11.5px;font-weight:700;color:var(--purple-dark);line-height:1.25">We accept most major insurances<br>and offer affordable self-pay rates.</p>

  <!-- Panel: cover -->
  <p class="abs on-purple center" style="left:760px;top:242px;width:346px;font-size:10.5px;font-weight:600;letter-spacing:.3px">A PERSONALIZED APPROACH TO SKIN CARE.</p>
  <p class="abs on-purple center" style="left:760px;top:262px;width:346px;font-size:10.5px">Results you can see. Care you can feel.</p>
  <div class="abs brand-name" style="left:885px;top:320px;width:96px">Corvellan<br><span style="font-size:11px">Skin &amp; Laser</span></div>
</section>

<!-- Inside of the trifold -->
<section class="sheet sheet--inside">
  <div class="photo" style="left:610px;top:160px;width:510px;height:260px" role="img" aria-label="Close-up beauty photo of a woman's face"></div>

  <svg class="shapes" width="1120" height="420" viewBox="0 0 1120 420">
    <path d="M0 0 H373 V205 Q190 262 0 232Z" fill="var(--purple)"/>
    <path d="M0 244 Q190 274 373 218" fill="none" stroke="var(--green)" stroke-width="7"/>
    <rect x="80" y="0" width="180" height="6" fill="var(--green)"/>
    <g fill="var(--lilac)">
      <circle cx="14" cy="40" r="4"/><circle cx="14" cy="64" r="4"/><circle cx="14" cy="88" r="4"/><circle cx="14" cy="112" r="4"/><circle cx="14" cy="136" r="4"/><circle cx="14" cy="160" r="4"/><circle cx="14" cy="184" r="4"/>
      <circle cx="387" cy="40" r="4"/><circle cx="387" cy="64" r="4"/><circle cx="387" cy="88" r="4"/><circle cx="387" cy="112" r="4"/><circle cx="387" cy="136" r="4"/>
      <circle cx="760" cy="40" r="4"/><circle cx="760" cy="64" r="4"/><circle cx="760" cy="88" r="4"/><circle cx="760" cy="112" r="4"/>
    </g>
    <circle cx="125" cy="238" r="52" fill="var(--white)" stroke="var(--purple)" stroke-width="7"/>
    <path d="M373 0 H746 V168 Q560 200 373 178Z" fill="var(--purple)"/>
    <path d="M373 186 Q560 210 746 176" fill="none" stroke="var(--lilac)" stroke-width="8"/>
    <rect x="470" y="0" width="170" height="6" fill="var(--green)"/>
    <path d="M746 0 H1120 V140 Q930 176 746 160Z" fill="var(--purple)"/>
    <path d="M746 168 Q930 186 1120 150" fill="none" stroke="var(--lilac)" stroke-width="8"/>
    <path d="M746 178 Q930 196 1120 160" fill="none" stroke="var(--green)" stroke-width="5"/>
    <rect x="850" y="0" width="170" height="6" fill="var(--green)"/>
    <rect x="388" y="338" width="342" height="76" fill="var(--purple)"/>
  </svg>
  <div class="fold" style="left:373px"></div>
  <div class="fold" style="left:746px"></div>

  <!-- Panel: cosmetic -->
  <h2 class="abs script heading on-purple" style="left:30px;top:14px">- Cosmetic services -</h2>
  <p class="abs body on-purple" style="left:30px;top:48px;width:325px;font-size:10px">Your skin is unique, so we take pride in our ability to provide personalized consultations and skin care analysis to set you up with the right treatments and products.</p>
  <ul class="abs ticks ticks--tight on-purple center" style="left:30px;top:90px;width:320px">
    <li>Chemical peels</li><li>Photofacial</li><li>Ultralift</li><li>Lumina</li><li>IPL</li>
    <li>Injectables and fillers<br><span style="font-weight:400">(Velvane, Lumaderm, Firmessa, Toxalin and Softrex)</span></li>
  </ul>
  <div class="abs script center" style="left:78px;top:220px;width:94px;font-size:17px;line-height:1;color:var(--purple)">Esthetic services</div>
  <ul class="abs ticks ticks--tight center" style="left:40px;top:294px;width:240px;color:var(--ink)">
    <li>Facials</li><li>Peels</li><li>Microdermabrasion</li><li>Body wraps</li><li>Waxing</li><li>Eyelash extensions</li>
  </ul>
  <p class="abs" style="left:30px;top:374px;width:330px;font-size:11px;font-weight:700;font-style:italic;color:var(--purple)">Elite-grade cosmeceutical products:</p>
  <p class="abs" style="left:30px;top:390px;width:330px;font-size:10px;line-height:1.3">Including Aurelle, Mira Sol, Clarté, Dermavia, Skin Notes, Lashera and much more.</p>

  <!-- Panel: medical -->
  <h2 class="abs script heading on-purple" style="left:400px;top:14px">- Medical services -</h2>
  <p class="abs body on-purple" style="left:400px;top:48px;width:330px;font-size:10px">We are leaders in the diagnosis of all skin conditions and offer trusted care for common skin concerns.</p>
  <ul class="abs ticks ticks--tight on-purple" style="left:430px;top:78px;width:140px">
    <li>Rashes</li><li>Acne</li><li>Warts</li><li>Skin tags</li><li>Moles</li><li>Psoriasis</li>
  </ul>
  <p class="abs on-purple" style="left:400px;top:160px;width:330px;font-size:9.5px;line-height:1.2">We're also involved in ongoing research for the treatment of psoriasis.</p>
  <h3 class="abs script" style="left:400px;top:200px;width:205px;font-size:17px;line-height:1.05;color:var(--purple)">* Skin cancer surveillance<br>&nbsp;&nbsp;and treatment</h3>
  <p class="abs" style="left:400px;top:240px;width:205px;font-size:10px;line-height:1.3">Skin cancer can form anywhere on the skin (even where the sun doesn't shine), so it's vital that a full body exam is done at least once a year.</p>
  <p class="abs center" style="left:400px;top:294px;width:205px;font-size:10px;line-height:1.25;font-weight:700;color:var(--purple)">We pride ourselves on thorough surveillance and commitment to your overall health.</p>
  <h3 class="abs script on-purple" style="left:400px;top:342px;font-size:16px">* Alternative care</h3>
  <p class="abs body on-purple" style="left:400px;top:362px;width:320px;font-size:9.5px;line-height:1.3">Your commitment to your health is the same as our commitment to you. We provide non-antibiotic acne treatment including botanicals, blue light and a combination of supplements to fit your personal lifestyle.</p>

  <!-- Panel: surgical -->
  <h2 class="abs script heading on-purple" style="left:775px;top:14px">- Surgical services -</h2>
  <p class="abs body on-purple" style="left:775px;top:48px;width:330px;font-size:10px">We have a skilled surgical team on site for minor procedures, removals and skin cancer care, with calm and careful support from start to finish.</p>
  <ul class="abs ticks on-purple" style="left:775px;top:104px;width:330px">
    <li>Mohs surgery <span style="font-weight:400">treatment includes reconstruction and care from your trusted healthcare team</span></li>
  </ul>
</section>

</body>
</html>
```